Fundraising Event Logistics and Strategy

We need a web design for our non-profit fundraising event strategy business. We help non-profits streamline gala and 'pre registered' event operations to maximize their funds raised. We would like a simple design, our company colors are dark blue and silver. The design should be clean and also allow for some partner logos. I have attached some current logo collateral. Company is Marlow Fenwick & Co dba GalaCrest, but neither logo has to be used.
Target Market(s)
Non Profit Organizations
Industry/Entity Type
Business
Number of Pages Required
3 page
Requirements
Must have
- Contact Us Form
- Partner Logos with Links

```html
<!DOCTYPE html>
<html lang="en">
<head>
<meta charset="utf-8">
<title>GalaCrest — Fundraising Event Logistics and Strategy</title>
<link rel="stylesheet" href="https://fonts.googleapis.com/css2?family=Open+Sans:wght@300;400;600;700&family=Raleway:wght@300;400;600&display=swap">
<style>
  :root {
    --blue: #1a5fb4;
    --blue-dark: #0f3f82;
    --blue-light: #5aa9f0;
    --navy: #1f2a3a;
    --charcoal: #2b2f36;
    --charcoal-deep: #22262c;
    --silver: #c9ccd1;
    --silver-light: #eef0f2;
    --partner: #d6d9dd;
    --text: #4a4f57;
    --muted: #8a9099;
    --white: #ffffff;
    --page: #ffffff;
  }
  * { box-sizing: border-box; margin: 0; padding: 0; }
  html, body { width: 1200px; height: 2400px; overflow: hidden; background: var(--page); }
  body { font-family: "Open Sans", Arial, sans-serif; color: var(--text); font-size: 14px; line-height: 1.55; }
  a { text-decoration: none; }
  .wrap { width: 1040px; height: 2400px; margin: 0 auto; display: flex; flex-direction: column; }

  .site-header { height: 90px; flex: none; display: flex; align-items: center; justify-content: space-between; }
  .brand { display: flex; align-items: center; gap: 10px; font-weight: 700; font-size: 24px; letter-spacing: 1px; color: var(--navy); }
  .brand-mark { width: 14px; height: 14px; background: var(--blue); }
  .btn { display: inline-block; background: var(--blue); color: var(--white); font-size: 13px; font-weight: 600; padding: 10px 26px; letter-spacing: .5px; border: none; }
  .btn-outline { background: transparent; border: 1px solid var(--white); color: var(--white); }

  .hero { position: relative; height: 430px; flex: none; background: linear-gradient(110deg, #4a5260 0%, #6b7380 45%, #9aa0a8 70%, #5d646f 100%); }
  .main-nav { position: absolute; top: 0; left: 0; right: 0; height: 40px; background: rgba(31,42,58,.85); display: flex; }
  .main-nav a { color: var(--white); font-size: 13px; font-weight: 600; padding: 0 22px; line-height: 40px; }
  .main-nav a.active { background: var(--blue); }
  .hero-copy { position: absolute; left: 40px; top: 100px; font-family: "Raleway", Arial, sans-serif; font-weight: 300; font-size: 48px; line-height: 1.08; color: #cfe3f7; }
  .hero-copy strong { font-weight: 400; color: var(--white); }
  .hero .btn { position: absolute; left: 40px; top: 330px; }

  .section-title { font-size: 15px; font-weight: 700; color: var(--navy); margin-bottom: 10px; }
  .about { padding: 34px 0 10px; flex: none; }
  .about p { font-size: 12.5px; color: var(--muted); margin-bottom: 12px; max-width: 1000px; }
  .cards { display: flex; gap: 30px; margin-top: 22px; }
  .card { flex: 1; }
  .card-media { height: 170px; }
  .card-media.one { background: linear-gradient(135deg, #e6e8ea, #b9bdc3); }
  .card-media.two { background: linear-gradient(135deg, #c7ccd3, #8d939c); }
  .card-media.three { background: linear-gradient(135deg, #dfe2e5, #9ea4ac); }
  .card-caption { text-align: center; font-size: 12px; color: var(--muted); margin-top: 10px; }

  .partners { flex: none; margin-top: 18px; display: flex; align-items: center; gap: 24px; }
  .partners-label { font-size: 12px; font-weight: 700; color: var(--navy); letter-spacing: .5px; width: 90px; }
  .partner-link { flex: 1; height: 44px; background: var(--partner); display: block; }

  .events { height: 290px; flex: none; background: linear-gradient(90deg, #3a4250 0%, #5a616c 55%, #c9c4bd 80%, #8e8a86 100%); position: relative; margin-top: 26px; }
  .events-inner { position: absolute; left: 40px; top: 30px; }
  .events h2 { font-size: 22px; font-weight: 700; color: var(--white); letter-spacing: 1px; }
  .events .event-name { color: var(--silver); font-size: 13px; margin: 12px 0 18px; }
  .countdown { display: flex; gap: 10px; }
  .count-box { width: 86px; height: 96px; background: var(--blue); color: var(--white); text-align: center; padding-top: 16px; }
  .count-box b { display: block; font-size: 34px; font-weight: 300; line-height: 1; }
  .count-box span { font-size: 11px; text-transform: uppercase; letter-spacing: 1px; }

  .contact { padding: 30px 0 0; flex: none; }
  .contact-info { font-size: 12.5px; color: var(--muted); margin-bottom: 22px; }
  .contact-info div { display: flex; align-items: center; gap: 8px; }
  .signup-title { font-size: 14px; font-weight: 700; color: var(--blue); border-bottom: 2px solid var(--blue); display: inline-block; margin-bottom: 14px; }
  .field label { display: block; font-size: 12px; color: var(--muted); margin-bottom: 4px; }
  .field .input { height: 32px; border: 1px solid var(--silver); margin-bottom: 12px; width: 620px; }
  .field .textarea { height: 120px; }
  .contact .btn { margin-top: 4px; padding: 8px 30px; }

  .cta-band { flex: none; margin-top: 38px; height: 120px; background: linear-gradient(100deg, var(--blue-light) 0%, var(--blue-light) 30%, var(--blue) 30%, var(--blue-dark) 100%); display: flex; align-items: center; padding: 0 40px; gap: 40px; }
  .cta-band p { color: var(--white); font-family: "Raleway", Arial, sans-serif; font-size: 20px; line-height: 1.2; width: 260px; }
  .cta-band .actions { display: flex; gap: 14px; align-items: center; margin-left: 70px; }
  .cta-band .or { color: var(--white); font-size: 13px; }

  .site-footer { background: var(--charcoal); flex: 1; padding: 34px 40px; display: flex; gap: 40px; }
  .footer-col { flex: 1; color: #9aa0a8; font-size: 12px; }
  .footer-col h3 { color: var(--white); font-size: 12.5px; font-weight: 700; margin-bottom: 12px; letter-spacing: .5px; }
  .footer-col li { list-style: none; margin-bottom: 6px; }
  .footer-input { height: 30px; background: #3a3f47; margin: 10px 0 8px; }
  .footer-bottom { flex: none; background: var(--charcoal-deep); height: 50px; display: flex; align-items: center; justify-content: space-between; padding: 0 40px; color: #7b818a; font-size: 11.5px; }
  .social { display: flex; gap: 10px; }
  .social span { width: 18px; height: 18px; border-radius: 50%; background: #5b616a; display: block; }
</style>
</head>
<body>
<div class="wrap">
  <header class="site-header">
    <div class="brand"><span class="brand-mark"></span>GalaCrest</div>
    <a class="btn" href="#contact">GET STARTED</a>
  </header>

  <section class="hero" role="img" aria-label="Photo of a businessman in a suit reaching across a desk">
    <nav class="main-nav">
      <a class="active" href="#">Home</a><a href="#about">About</a><a href="#contact">Contact us</a>
    </nav>
    <div class="hero-copy">we are<br><strong>turning the way</strong><br>you think<br>for the next...</div>
    <a class="btn" href="#about">LEARN MORE</a>
  </section>

  <section class="about" id="about">
    <h2 class="section-title">About us</h2>
    <p>We help non-profit organizations plan and run gala and pre-registered fundraising events with less effort and better results. Our team handles logistics, bidding, check-in and reporting so your staff can focus on guests and your mission, while every step is built to raise more funds.</p>
    <p>From the first planning call to the final thank-you letter, we bring clear strategy, proven tools and calm people to every event. We work beside your board and volunteers, train them on the night, and share simple numbers afterwards so you can see what worked and grow your results next year.</p>
    <div class="cards">
      <div class="card"><div class="card-media one" role="img" aria-label="Photo of a team planning at a whiteboard"></div><div class="card-caption">Event Strategy</div></div>
      <div class="card"><div class="card-media two" role="img" aria-label="Photo of people working together at a table"></div><div class="card-caption">Gala Logistics</div></div>
      <div class="card"><div class="card-media three" role="img" aria-label="Photo of a presenter at a meeting"></div><div class="card-caption">Donor Registration</div></div>
    </div>
  </section>

  <section class="partners" aria-label="Partners">
    <span class="partners-label">PARTNERS</span>
    <a class="partner-link" href="#" role="img" aria-label="Partner logo"></a>
    <a class="partner-link" href="#" role="img" aria-label="Partner logo"></a>
    <a class="partner-link" href="#" role="img" aria-label="Partner logo"></a>
    <a class="partner-link" href="#" role="img" aria-label="Partner logo"></a>
    <a class="partner-link" href="#" role="img" aria-label="Partner logo"></a>
  </section>

  <section class="events" role="img" aria-label="Photo of a businesswoman at a desk behind the events panel">
    <div class="events-inner">
      <h2>UPCOMING EVENTS</h2>
      <div class="event-name">Spring Charity Gala<br>Westfield Hall</div>
      <div class="countdown">
        <div class="count-box"><b>12</b><span>Days</span></div>
        <div class="count-box"><b>08</b><span>Hours</span></div>
        <div class="count-box"><b>31</b><span>Mins</span></div>
        <div class="count-box"><b>45</b><span>Secs</span></div>
      </div>
    </div>
  </section>

  <section class="contact" id="contact">
    <h2 class="section-title">GET IN TOUCH</h2>
    <div class="contact-info">
      <div><svg width="12" height="12" viewBox="0 0 12 12"><path d="M6 0a4 4 0 0 0-4 4c0 3 4 8 4 8s4-5 4-8a4 4 0 0 0-4-4zm0 5.5A1.5 1.5 0 1 1 6 2.5a1.5 1.5 0 0 1 0 3z" fill="#8a9099"/></svg>Address: 14 Harbor Lane, Westfield, Ohio</div>
      <div><svg width="12" height="12" viewBox="0 0 12 12"><path d="M2 1l2 0 1 3-1.5 1a7 7 0 0 0 3.5 3.5L8 7l3 1v2a1 1 0 0 1-1 1A9 9 0 0 1 1 2a1 1 0 0 1 1-1z" fill="#8a9099"/></svg>Tel: +1 555 010 2040</div>
      <div><svg width="12" height="12" viewBox="0 0 12 12"><rect x="0.5" y="2" width="11" height="8" fill="none" stroke="#8a9099"/><path d="M0.5 2l5.5 4 5.5-4" fill="none" stroke="#8a9099"/></svg>Email: hello@galacrest.example</div>
    </div>
    <div class="signup-title">SIGN UP</div>
    <div class="field"><label>Your Name (required)</label><div class="input"></div></div>
    <div class="field"><label>Your Email (required)</label><div class="input"></div></div>
    <div class="field"><label>Subject</label><div class="input"></div></div>
    <div class="field"><label>Your Message</label><div class="input textarea"></div></div>
    <a class="btn" href="#">Send</a>
  </section>

  <section class="cta-band">
    <p>Ready to raise more at your next event?</p>
    <div class="actions">
      <a class="btn btn-outline" href="#">REQUEST A DEMO</a>
      <span class="or">or</span>
      <a class="btn btn-outline" href="#contact">CONTACT US TODAY</a>
    </div>
  </section>

  <footer class="site-footer">
    <div class="footer-col"><h3>ABOUT GALACREST</h3><p>Fundraising event logistics and strategy for non-profits across the region, from gala nights to registered events.</p></div>
    <div class="footer-col"><h3>QUICK LINKS</h3><ul><li>Home</li><li>About</li><li>Events</li><li>Contact us</li></ul></div>
    <div class="footer-col"><h3>OUR SERVICES</h3><ul><li>Event Strategy</li><li>Mobile Bidding</li><li>Guest Check-in</li><li>Reporting</li></ul></div>
    <div class="footer-col"><h3>NEWSLETTER</h3><p>Get event tips in your inbox.</p><div class="footer-input"></div><a class="btn" href="#">Subscribe</a></div>
  </footer>
  <div class="footer-bottom">
    <span>© Marlow Fenwick &amp; Co. All rights reserved.</span>
    <div class="social"><span></span><span></span><span></span><span></span></div>
  </div>
</div>
</body>
</html>
```